Finch Haulage Ltd

We need an A5 size (UK size) flyer to advertise our new business which is called Finch Haulage.
Domestic and Commercial Waste Clearance Services.
Please have the question in bold "Do you have a pile of junk you need to dispose of?"
We collect all kinds of junk or rubbish from homes and businesses across Kent, Sussex and South London.
No fuss, no mess!
A low cost, hassle free alternative to skip hire.
Licensed by the Landcare Board and fully insured (this can be in small print at the bottom).
Please put the Recycle symbol somewhere.
Our tagline on our vehicle is "We Clear More, For Less!"
We'd like the flyer to be bold and eye-catching (to catch the eye of the homeowner or business owner while it's sitting on their doormat).
We need our telephone, website and email to be prominent. Maybe saying "Call today for a free quote"
Tel. 01734 586019
Email: info@finchhaulage.example.co.uk
www.finchhaulage.example.co.uk
Target Market(s)
Our market will be homes and small businesses around Kent, Sussex and South London.

```html
<!DOCTYPE html>
<html lang="en">
<head>
<meta charset="utf-8">
<title>Finch Haulage – Waste Clearance Flyer</title>
<link rel="stylesheet" href="https://fonts.googleapis.com/css2?family=Open+Sans:ital,wdth,wght@0,75..100,300..800;1,75..100,300..800&display=swap">
<style>
  :root {
    --backdrop: #58595b;
    --paper: #ffffff;
    --panel: #efefef;
    --green: #27ae55;
    --green-soft: #a8dcb4;
    --ink: #555555;
    --ink-dark: #3f3f3f;
  }
  * { margin: 0; padding: 0; box-sizing: border-box; }
  html, body {
    width: 1200px; height: 900px; overflow: hidden;
    background: var(--backdrop);
    font-family: "Open Sans", Arial, sans-serif;
  }
  .flyer {
    position: absolute; left: 312px; top: 41px;
    width: 576px; height: 817px;
    background: var(--panel);
    overflow: hidden;
  }
  .flyer__top-band {
    position: absolute; left: 0; top: 0; width: 100%; height: 67px;
    background: var(--paper);
    border-bottom: 1px solid #dcdcdc;
  }
  .flyer__bottom-band {
    position: absolute; left: 0; bottom: 0; width: 100%; height: 125px;
    background: var(--green);
  }
  .brand-name {
    position: absolute; left: 0; top: 80px; width: 100%;
    text-align: center;
    font-size: 60px; font-weight: 700; font-stretch: 75%;
    letter-spacing: 2px; color: var(--ink);
  }
  .service-tag {
    position: absolute; left: 54px; top: 197px; width: 468px; height: 28px;
    background: var(--green); border-radius: 4px;
    color: #fff; text-align: center;
    font-size: 19px; font-weight: 700; font-stretch: 75%; line-height: 28px;
  }
  .headline {
    position: absolute; left: 0; top: 254px; width: 100%;
    text-align: center; color: var(--ink);
    font-size: 42px; font-weight: 700; font-stretch: 75%;
    line-height: 42px;
  }
  .intro {
    position: absolute; left: 0; top: 360px; width: 100%;
    text-align: center; color: var(--ink);
    font-size: 16.3px; line-height: 24.3px; font-weight: 400;
  }
  .intro strong { font-weight: 700; color: var(--ink-dark); }
  .tagline {
    position: absolute; left: 106px; top: 512px; width: 365px; height: 51px;
    background: var(--green); border-radius: 3px;
    box-shadow: 5px 5px 0 var(--green-soft);
    color: #fff; text-align: center;
    font-size: 27px; font-weight: 700; font-stretch: 75%; line-height: 51px;
  }
  .contact-box {
    position: absolute; left: 54px; top: 609px; width: 468px; height: 126px;
    background: var(--paper);
    border: 4px solid var(--green-soft); border-radius: 8px;
  }
  .contact-box__title {
    position: absolute; left: 0; top: 12px; width: 100%;
    text-align: center; color: var(--green);
    font-size: 27px; font-weight: 700; font-stretch: 75%;
  }
  .contact-box__phone {
    position: absolute; left: 20px; top: 66px;
    display: flex; align-items: center; gap: 8px;
    color: var(--ink); font-size: 28px; font-weight: 700; font-stretch: 75%;
    white-space: nowrap;
  }
  .contact-box__divider {
    position: absolute; left: 212px; top: 64px; width: 2px; height: 38px;
    background: var(--green);
  }
  .contact-box__details {
    position: absolute; left: 224px; top: 63px;
    color: var(--ink); font-size: 12.5px; font-weight: 700; font-stretch: 75%;
    line-height: 20px; white-space: nowrap;
  }
  .recycle-mark {
    position: absolute; left: 273px; top: 744px;
  }
  .licence-note {
    position: absolute; left: 0; top: 775px; width: 100%;
    text-align: center; color: #fff;
    font-size: 15px; font-style: italic;
  }
</style>
</head>
<body>
  <main class="flyer">
    <div class="flyer__top-band"></div>
    <div class="flyer__bottom-band"></div>

    <div class="brand-name">FINCH HAULAGE</div>

    <div class="service-tag">DOMESTIC AND COMMERCIAL WASTE CLEARANCE SERVICES</div>

    <h1 class="headline">DO YOU HAVE A PILE OF JUNK,<br>YOU NEED TO DISPOSE OF?</h1>

    <p class="intro">
      WE COLLECT ALL KINDS OF JUNK OR RUBBISH<br>
      FROM HOMES &amp; BUSINESSES<br>
      ACROSS KENT, SUSSEX AND SOUTH LONDON.<br>
      <strong>NO FUSS, NO MESS!</strong><br>
      <strong>A LOW COST, HASSLE FREE ALTERNATIVE TO SKIP HIRE.</strong>
    </p>

    <div class="tagline">"WE CLEAR MORE, FOR LESS!"</div>

    <section class="contact-box">
      <h2 class="contact-box__title">CALL TODAY FOR A FREE QUOTE</h2>
      <div class="contact-box__phone">
        <svg width="24" height="24" viewBox="0 0 24 24" aria-hidden="true">
          <rect width="24" height="24" rx="4" fill="#27ae55"/>
          <path d="M8.2 5.5l2 2.6c.3.4.3.9-.1 1.3l-1 1c.8 1.7 2 2.9 3.6 3.7l1-1c.4-.4.9-.4 1.3-.1l2.6 2c.4.3.4.9.1 1.3l-1 1.2c-.6.7-1.6.9-2.4.5-3.4-1.6-6-4.2-7.6-7.6-.4-.8-.2-1.8.5-2.4l1.2-1c.4-.3 1-.3 1.3.1z" fill="#fff"/>
        </svg>
        <span>01734 586019</span>
      </div>
      <div class="contact-box__divider"></div>
      <div class="contact-box__details">
        EMAIL: INFO@FINCHHAULAGE.EXAMPLE.CO.UK<br>
        WWW.FINCHHAULAGE.EXAMPLE.CO.UK
      </div>
    </section>

    <svg class="recycle-mark" width="30" height="30" viewBox="0 0 30 30" aria-label="Recycle symbol" role="img">
      <g fill="none" stroke="#fff" stroke-width="3.2" stroke-linejoin="round">
        <path d="M11 6 L15 3 L19 9"/>
        <path d="M23 13 L26 20 L20 25"/>
        <path d="M12 25 L5 24 L4 17"/>
      </g>
      <g fill="#fff">
        <path d="M16 11 L22 10 L20 15 Z"/>
        <path d="M17 21 L22 26 L17 29 Z"/>
        <path d="M8 11 L2 14 L5 18 Z"/>
      </g>
    </svg>

    <p class="licence-note">Licensed by the Landcare Board and fully insured.</p>
  </main>
</body>
</html>
```